Entertainer/Dancer Business Cards

Devon Marsh is an up and coming entertainer from Baltimore, Maryland currently relocating to Los Angeles, California for a dance opportunity at the renowned Ruthie Calder Dance Studio.
This young man needs to promote himself and his skills in a populous and competitive city.
Hopefully, this card will set him apart from the tons of entertainers in L.A.
It will passed out to fellow entertainers, agents, and random people looking for talent.

I have uploaded an image of the dancer, it is not necessary to use this image; however it is in PSD format if one should decide to incorporate it somehow and would like to make changes.

Industry/Entity Type

Business

Contact Information for Business Card

Devon Marsh
(line 1) Dancer Choreographer Instructor Singer/Songwriter
(line 2) Ballet-Modern-Urban
devonmarsh00@fernpost.com
410-582-7146

Requirements
Nice to have

• Open to an all typography card.
Should not have
• No logo; just name: Devon Marsh
Devon is a guy (in case you were wondering :D )
Please no ballet/pointe shoes in design

```html
<!DOCTYPE html>
<html lang="en">
<head>
<meta charset="utf-8">
<title>Devon Marsh — Business Cards</title>
<link rel="stylesheet" href="https://fonts.googleapis.com/css2?family=Orbitron:wght@800;900&family=Lato:wght@400;700&display=swap">
<style>
  :root {
    --backdrop: #5e4a33;
    --card: #0d0e10;
    --card-edge: #1a1c1f;
    --accent-light: #8fdcf2;
    --accent: #3fb6c8;
    --accent-deep: #17939f;
    --text-soft: #d6d8da;
    --text-white: #f2f3f4;
  }
  * { box-sizing: border-box; margin: 0; padding: 0; }
  html, body {
    width: 1200px;
    height: 1000px;
    overflow: hidden;
    background: var(--backdrop);
  }
  .stage {
    position: relative;
    width: 1200px;
    height: 1000px;
  }
  .card {
    position: absolute;
    width: 720px;
    height: 410px;
    background: var(--card);
    border: 1px solid var(--card-edge);
    box-shadow: 0 14px 30px rgba(0,0,0,0.45);
    overflow: hidden;
  }
  .card__stripe {
    position: absolute;
    left: 0; top: 0; bottom: 0;
    width: 22px;
    background: linear-gradient(180deg, var(--accent-light), var(--accent-deep));
  }
  .display-name {
    font-family: "Orbitron", sans-serif;
    font-weight: 900;
    text-transform: uppercase;
    background: linear-gradient(180deg, var(--accent-light) 0%, var(--accent) 55%, var(--accent-deep) 100%);
    -webkit-background-clip: text;
    background-clip: text;
    color: transparent;
    line-height: 1;
  }

  /* Front */
  .card--front { left: 130px; top: 60px; }
  .card--front .display-name {
    position: absolute;
    left: 120px;
    top: 85px;
    font-size: 112px;
    letter-spacing: 2px;
  }
  .card--front .display-name span { display: block; }
  .card--front .display-name span + span { margin-top: 22px; }

  /* Back */
  .card--back { left: 350px; top: 530px; text-align: center; }
  .card--back .card__content {
    position: absolute;
    left: 22px; right: 0; top: 58px;
  }
  .card--back .display-name {
    font-size: 54px;
    letter-spacing: 1px;
  }
  .roles {
    margin-top: 18px;
    font-family: "Lato", sans-serif;
    font-size: 20px;
    color: var(--text-soft);
  }
  .styles {
    margin-top: 16px;
    font-family: "Lato", sans-serif;
    font-weight: 700;
    font-size: 25px;
    letter-spacing: 3px;
    color: var(--accent);
  }
  .contact {
    margin-top: 52px;
    font-family: "Lato", sans-serif;
    font-weight: 700;
    font-size: 25px;
    letter-spacing: 2px;
    line-height: 1.45;
    color: var(--text-white);
  }
</style>
</head>
<body>
  <main class="stage">
    <section class="card card--front" aria-label="Business card front">
      <div class="card__stripe"></div>
      <h1 class="display-name"><span>Devon</span><span>Marsh</span></h1>
    </section>

    <section class="card card--back" aria-label="Business card back">
      <div class="card__stripe"></div>
      <div class="card__content">
        <h2 class="display-name">Devon Marsh</h2>
        <p class="roles">Dancer, Choreographer, Instructor, Singer/Songwriter.</p>
        <p class="styles">BALLET - MODERN - URBAN</p>
        <div class="contact">
          <p>Phone: 410-582-7146</p>
          <p>Email: devonmarsh00@fernpost.com</p>
        </div>
      </div>
    </section>
  </main>
</body>
</html>
```